KAZ Freightworks #ALLKAZ Business Cards & Letterhead

I am looking to business cards designed for our organization. We are currently undergoing a small re-branding that is taking place. Our organization is called KAZ Freightworks and we are headquartered in Phoenix, AZ. We primarily provide transportation and logistics services to the Meridel Parcel Bureau who is our largest customer. I would like to see a design that incorporates name, title, contact info, website, and address (this will be different depending on the employee). I would also like to see some color on the business card using our logo colors or a variation. I would like our logo on the back of the business card with the website displayed. The final design should communicate that we are a next generation transportation operate that focuses on being driver-first, customer-centric, innovative, and sustainable.We would also like our #ALLKAZ catch phrase incorporated as well.
Updates

Decision maker traveling outside of the country until Monday, November 25th.

Target Market(s)

Transportation & Logistics

Industry/Entity Type

Trucking Company

Contact Information for Business Card

-First and Last Name
-Position Title
-Contact Phone
-Contact Email
-Physical Address

Font styles to use
Serif

Colors

Designer to choose colors to be used in the design.

Requirements
Must have
• -KAZ logo prominently displayed
• -#ALLKAZ catch phrase used
• -Some amount of color, design gradient, etc.
• -Logo on the back with website listed (https://www.kazfreightco.example)

```html
<!DOCTYPE html>
<html lang="en">
<head>
<meta charset="utf-8">
<title>KAZ Freightworks Stationery</title>
<link rel="stylesheet" href="https://fonts.googleapis.com/css2?family=Barlow+Condensed:ital,wght@1,500&family=Roboto:wght@400;700&display=swap">
<style>
:root{
  --bg:#999999;
  --paper:#ffffff;
  --green:#82c341;
  --ink:#023a46;
  --grey:#6b6b6b;
}
*{margin:0;padding:0;box-sizing:border-box}
html,body{width:1200px;height:763px;overflow:hidden;background:var(--bg)}
body{position:relative;font-family:"Roboto",Arial,sans-serif}
.card{position:absolute;left:91px;width:399px;height:234px;border-radius:12px;overflow:hidden;border:1px solid #7d7d7d}
.card-front{top:134px;background:var(--paper)}
.card-back{top:390px;background:var(--green)}
.tagline{font-family:"Barlow Condensed","Arial Narrow",sans-serif;font-style:italic;font-weight:500;color:var(--green);white-space:nowrap}
.card-front .tagline{position:absolute;left:22px;top:20px;font-size:13px}
.person{position:absolute;left:22px;top:64px}
.person-name{font-weight:700;font-size:13.5px;color:var(--ink);letter-spacing:.2px}
.person-title{font-size:9.5px;color:var(--green)}
.address{position:absolute;left:22px;top:98px;font-size:9.5px;line-height:12px;color:var(--grey)}
.contacts{position:absolute;left:22px;top:130px;list-style:none;font-size:9.5px;line-height:13.2px;color:var(--grey)}
.contacts li{display:flex;align-items:center;gap:3px}
.contacts svg{width:8px;height:8px;fill:var(--green)}
.hashtag{font-weight:700;color:var(--ink)}
.card-front .hashtag{position:absolute;left:23px;top:200px;font-size:9.5px}

.wordmark{position:absolute;display:flex;align-items:center;justify-content:center;font-weight:700;line-height:1}
.wordmark .dot{border-radius:50%;flex:none}
.card-front .wordmark{left:180px;top:12px;width:210px;height:210px;gap:10px;color:var(--ink);font-size:72px}
.card-front .wordmark .dot{width:22px;height:22px;background:var(--green)}
.card-back .wordmark{left:0;right:0;top:68px;height:99px;gap:7px;color:var(--paper);font-size:34px}
.card-back .wordmark .dot{width:12px;height:12px;background:var(--paper)}
.card-back .site{position:absolute;left:0;right:0;top:208px;text-align:center;color:var(--paper);font-size:11px}

.letterhead{position:absolute;left:523px;top:17px;width:570px;height:726px;background:var(--paper);border:1px solid #888}
.letterhead .wordmark{left:0;right:0;top:23px;height:56px;gap:5px;color:var(--ink);font-size:22px}
.letterhead .wordmark .dot{width:8px;height:8px;background:var(--green)}
.letterhead .tagline{position:absolute;left:0;right:0;top:80px;text-align:center;font-size:7.5px}
.letterhead .hashtag{position:absolute;left:0;right:0;top:675px;text-align:center;color:var(--green);font-size:11px}
.footer-rule{position:absolute;left:0;right:0;top:694px;height:3px;background:var(--ink)}
.footer-band{position:absolute;left:0;right:0;top:697px;height:29px;background:var(--green);display:flex;align-items:center;justify-content:center;gap:4px;color:var(--paper);font-size:8.3px;white-space:nowrap}
.footer-band svg{width:7px;height:7px;fill:var(--paper);margin-left:3px}
</style>
</head>
<body>
<svg width="0" height="0" style="position:absolute">
  <symbol id="icon-phone" viewBox="0 0 10 10"><path d="M2.2 0.5 3.6 2.6 2.7 3.6C3.3 5 4.9 6.6 6.4 7.3L7.4 6.4 9.5 7.8 8.7 9.3C4.8 9.2 0.8 5.2 0.7 1.3Z"/></symbol>
  <symbol id="icon-mail" viewBox="0 0 10 10"><path d="M0 2h10v6H0z"/><path d="M0.6 2.4 5 5.5 9.4 2.4" stroke="#fff" stroke-width="0.8" fill="none"/></symbol>
  <symbol id="icon-web" viewBox="0 0 10 10"><path d="M5 0.5A4.5 4.5 0 1 0 5 9.5 4.5 4.5 0 1 0 5 0.5ZM5 1.5C5.8 2.3 6.2 3.5 6.3 4.5H3.7C3.8 3.5 4.2 2.3 5 1.5ZM1.6 4.5C1.8 3 2.8 1.9 4 1.6 3.3 2.4 2.9 3.4 2.8 4.5ZM7.2 4.5C7.1 3.4 6.7 2.4 6 1.6 7.2 1.9 8.2 3 8.4 4.5ZM1.6 5.5H2.8C2.9 6.6 3.3 7.6 4 8.4 2.8 8.1 1.8 7 1.6 5.5ZM3.7 5.5H6.3C6.2 6.5 5.8 7.7 5 8.5 4.2 7.7 3.8 6.5 3.7 5.5ZM7.2 5.5H8.4C8.2 7 7.2 8.1 6 8.4 6.7 7.6 7.1 6.6 7.2 5.5Z"/></symbol>
</svg>

<section class="card card-front">
  <p class="tagline">Transportation and Logistics Services</p>
  <div class="person">
    <p class="person-name">JANE DORAN</p>
    <p class="person-title">President</p>
  </div>
  <p class="address">4170 North Cactus Ridge Road<br>Glendale, AZ 85301</p>
  <ul class="contacts">
    <li><svg><use href="#icon-phone"/></svg>555-014-2290</li>
    <li><svg><use href="#icon-mail"/></svg>info@kazfreightco.example</li>
    <li><svg><use href="#icon-web"/></svg>www.kazfreightco.example</li>
  </ul>
  <p class="hashtag">#ALLKAZ</p>
  <div class="wordmark"><span class="dot"></span><span>KAZ</span></div>
</section>

<section class="card card-back">
  <div class="wordmark"><span class="dot"></span><span>KAZ</span></div>
  <p class="site">www.kazfreightco.example</p>
</section>

<section class="letterhead">
  <div class="wordmark"><span class="dot"></span><span>KAZ</span></div>
  <p class="tagline">Transportation and Logistics Services</p>
  <p class="hashtag">#ALLKAZ</p>
  <div class="footer-rule"></div>
  <div class="footer-band">
    <span>4170 North Cactus Ridge Road, Glendale, AZ 85301</span>
    <svg><use href="#icon-phone"/></svg><span>555-014-2290</span>
    <svg><use href="#icon-mail"/></svg><span>info@kazfreightco.example</span>
    <svg><use href="#icon-web"/></svg><span>www.kazfreightco.example</span>
  </div>
</section>
</body>
</html>
```